Therapist website

I need a sqaure space web design for my therapy practice. I need a home page, a services page with 4 subpages, an about me, an insurnace page, a contact page, an EMDR page

```html
<!DOCTYPE html>
<html lang="en">
<head>
<meta charset="utf-8">
<title>Willowmere Counseling</title>
<link rel="stylesheet" href="https://fonts.googleapis.com/css2?family=Arimo:wght@400;700&display=swap">
<style>
:root{
  --teal:#1b9ea8;
  --teal-text:#17b5bf;
  --ink:#111;
  --muted:#555;
  --band:#f3f3f3;
  --line:#e6e6e6;
  --white:#fff;
}
*{box-sizing:border-box;margin:0;padding:0}
html,body{width:1200px;height:1200px;overflow:hidden;background:var(--white);font-family:"Arimo",Helvetica,Arial,sans-serif;color:var(--ink)}
.page{position:absolute;left:346px;top:0;width:507px;height:1200px;background:var(--white)}
.abs{position:absolute}
.btn{position:absolute;border:1px solid var(--teal);border-radius:10px;color:var(--teal);font-size:5.6px;display:flex;align-items:center;justify-content:center;letter-spacing:.2px;background:transparent}
.small{font-size:4.6px;line-height:9px;color:var(--ink)}
.accent{color:var(--teal-text);font-weight:700}

/* hero */
.hero-photo{left:0;top:0;width:507px;height:250px;background:linear-gradient(180deg,#eef0ee 0%,#e3e6e3 70%,#c9d3b8 88%,#8fa466 100%)}
.hero-eyebrow{left:64px;top:66px;font-size:6.2px;letter-spacing:1.6px}
.hero-title{left:64px;top:77px;font-size:16px;letter-spacing:.2px}
.hero-text{left:64px;top:102px;width:150px;font-size:4.2px;line-height:8px}

/* nav */
.brand{left:26px;top:266px;display:flex;align-items:center;gap:4px;font-size:7px;color:var(--teal);letter-spacing:.6px}
.brand-dot{width:8px;height:8px;border-radius:50%;background:var(--teal)}
.nav{left:0;top:274px;font-size:5.8px;letter-spacing:2.2px}
.divider{left:28px;top:303px;width:452px;height:1px;background:var(--line)}

/* sections */
.section-title{left:0;width:507px;text-align:center;font-size:16px}
.section-text{left:0;width:507px;text-align:center;font-size:4.6px;line-height:9px}
.services{left:0;top:454px;width:507px;height:264px;background:var(--band)}
.ring{position:absolute;width:75px;height:75px;border:2px solid var(--teal);border-radius:50%;display:flex;align-items:center;justify-content:center}
.svc-name{position:absolute;width:110px;text-align:center;font-size:7.4px;color:var(--teal-text);font-weight:700}
.svc-text{position:absolute;width:110px;text-align:center;font-size:4.6px;line-height:9px;color:var(--muted)}
.svc-link{position:absolute;width:110px;text-align:center;font-size:5.6px;color:var(--teal-text);font-weight:700}

.ins-photo{left:239px;top:716px;width:266px;height:206px;background:linear-gradient(135deg,#6f7a3a 0%,#4f5e2e 40%,#2f3a2a 70%,#b07a2a 100%)}
.ins-title{left:28px;top:760px;font-size:16px;color:var(--teal-text);font-weight:700}
.ins-text{left:28px;top:788px;width:192px;font-size:4.6px;line-height:9.2px}

.cta{left:0;top:922px;width:507px;height:142px;background:var(--teal)}
.cta-title{left:0;top:24px;width:507px;text-align:center;color:var(--white);font-size:19px;line-height:32px}
.cta-btn{left:205px;top:92px;width:98px;height:17px;background:var(--white);border-radius:9px;color:var(--teal);font-size:5.4px;display:flex;align-items:center;justify-content:center;box-shadow:0 1px 2px rgba(0,0,0,.15)}

.foot-h{font-size:7.6px;font-weight:700}
.foot-t{font-size:4.8px;line-height:9px;color:#222}
.contact-row{display:flex;align-items:center;gap:6px;font-size:4.8px;height:12px}
.social{display:flex;gap:3px}
.social span{width:9px;height:9px;border-radius:50%;background:var(--teal)}
.copy{left:0;top:1178px;width:507px;height:22px;background:#eee;font-size:4.8px;text-align:center;line-height:22px}
</style>
</head>
<body>
<div class="page">

  <!-- hero -->
  <div class="abs hero-photo" role="img" aria-label="Photo of a joyful child jumping above tall grass against a pale sky"></div>
  <div class="abs hero-eyebrow">WELCOME TO</div>
  <div class="abs hero-title">WILLOWMERE</div>
  <p class="abs hero-text">Holisticly build progressive e-markets without long-term high-impact e-tailers. Intrinsicly e-enable cross-unit quality vectors without team building ROI.</p>
  <div class="btn" style="left:64px;top:136px;width:64px;height:16px">CONTACT US</div>

  <!-- navigation -->
  <div class="abs brand"><span class="brand-dot"></span>WILLOWMERE</div>
  <div class="abs nav">
    <span class="abs" style="left:195px">HOME</span>
    <span class="abs" style="left:240px;white-space:nowrap">ABOUT ME</span>
    <span class="abs" style="left:306px">INSURNACE</span>
    <span class="abs" style="left:379px">EMDR</span>
  </div>
  <div class="btn" style="left:419px;top:269px;width:63px;height:16px">CONTACT US</div>
  <div class="abs divider"></div>

  <!-- about -->
  <h2 class="abs section-title" style="top:328px;font-weight:400"><span class="accent">About</span> Me</h2>
  <p class="abs section-text" style="top:356px;padding:0 108px">Progressively fabricate enterprise-wide catalysts for change and high standards in testing procedures. Authoritatively re-engineer cooperative infrastructures for interdependent best practices. Objectively morph prospective content and turnkey mindshare. Dynamically embrace scalable communities whereas flexible solutions. Appropriately create superior e-commerce whereas bleeding-edge growth strategies.</p>
  <div class="btn" style="left:222px;top:403px;width:63px;height:16px">LEARN MORE</div>

  <!-- services -->
  <div class="abs services">
    <h2 class="abs section-title" style="top:32px;font-weight:400">Our <span class="accent">Services</span></h2>
    <p class="abs section-text" style="top:60px;padding:0 108px">Progressively fabricate enterprise-wide catalysts for change and high standards in testing procedures. Authoritatively re-engineer cooperative infrastructures for interdependent best practices.</p>

    <div class="ring" style="left:43px;top:92px">
      <svg width="22" height="24" viewBox="0 0 22 24" fill="none" stroke="#1b9ea8" stroke-width="2"><circle cx="11" cy="4" r="3" fill="#1b9ea8" stroke="none"/><path d="M3 11h16M11 9v6M6 20c0-4 10-4 10 0M7 14l-2 6M15 14l2 6"/></svg>
    </div>
    <div class="ring" style="left:156px;top:92px">
      <svg width="22" height="26" viewBox="0 0 22 26" fill="none" stroke="#1b9ea8" stroke-width="1.6"><circle cx="11" cy="10" r="7"/><path d="M4 8c3-5 11-5 14 0M8 22l3-2 3 2M8 24l3-2 3 2"/></svg>
    </div>
    <div class="ring" style="left:269px;top:92px">
      <svg width="26" height="26" viewBox="0 0 26 26" fill="none" stroke="#1b9ea8" stroke-width="2"><path d="M7 3v12h12l4 4M7 15l-2 5h16"/><circle cx="8" cy="22" r="2"/><circle cx="19" cy="22" r="2"/></svg>
    </div>
    <div class="ring" style="left:381px;top:92px">
      <svg width="28" height="26" viewBox="0 0 28 26" fill="none" stroke="#1b9ea8" stroke-width="2.2"><path d="M14 2l5 3v6l-5 3-5-3V5z" fill="#1b9ea8"/><path d="M3 10v8l6 6M25 10v8l-6 6M7 14l4 4M21 14l-4 4"/></svg>
    </div>

    <div class="svc-name" style="left:26px;top:186px">Child and Adolescent</div>
    <div class="svc-name" style="left:139px;top:186px">Adult</div>
    <div class="svc-name" style="left:252px;top:186px">Special Needs Parenting</div>
    <div class="svc-name" style="left:364px;top:186px">Foster Care and Adoption</div>

    <p class="svc-text" style="left:26px;top:200px">Progressively fabricate wide catalysts for change fabricate</p>
    <p class="svc-text" style="left:139px;top:200px">Progressively fabricate wide catalysts for change fabricate</p>
    <p class="svc-text" style="left:252px;top:200px">Progressively fabricate wide catalysts for change fabricate</p>
    <p class="svc-text" style="left:364px;top:200px">Progressively fabricate wide catalysts for change fabricate</p>

    <div class="svc-link" style="left:26px;top:226px">Learn More &rarr;</div>
    <div class="svc-link" style="left:139px;top:226px">Learn More &rarr;</div>
    <div class="svc-link" style="left:252px;top:226px">Learn More &rarr;</div>
    <div class="svc-link" style="left:364px;top:226px">Learn More &rarr;</div>
  </div>

  <!-- insurance -->
  <h2 class="abs ins-title">Insurance</h2>
  <p class="abs ins-text">Progressively fabricate enterprise-wide catalysts for change and high standards in testing procedures. Authoritatively re-engineer cooperative infrastructures for interdependent best practices. Objectively morph prospective content and turnkey mindshare. Dynamically embrace scalable communities whereas flexible solutions. Appropriately create superior e-commerce whereas bleeding-edge growth strategies.</p>
  <div class="btn" style="left:28px;top:854px;width:63px;height:16px">LEARN MORE</div>
  <div class="abs ins-photo" role="img" aria-label="Photo of a smiling family with a young child outdoors among autumn trees"></div>

  <!-- call to action -->
  <div class="abs cta">
    <h2 class="abs cta-title" style="font-weight:400">Don't Wait to Get the<br>Help You Need</h2>
    <div class="abs cta-btn">BOOK AN APPOINTMENT</div>
  </div>

  <!-- footer -->
  <div class="abs foot-h" style="left:73px;top:1086px">About Us</div>
  <p class="abs foot-t" style="left:73px;top:1105px;width:120px">Progressively fabricate enterprise-wide catalysts for change and high standards in testing procedures. Authoritatively re-engineer cooperative infrastructures for interdependent best practices.</p>

  <div class="abs foot-h" style="left:243px;top:1086px">Quick Links</div>
  <p class="abs foot-t" style="left:243px;top:1105px">Home<br>About me<br>Insurnace<br>EMDR<br>Contact us</p>

  <div class="abs foot-h" style="left:341px;top:1086px">Contact Details</div>
  <div class="abs" style="left:341px;top:1103px">
    <div class="contact-row"><svg width="6" height="6" viewBox="0 0 10 10"><path d="M2 1l2 2-1 2 2 2 2-1 2 2-2 2C4 9 1 6 0 3z" fill="#333"/></svg>555 010 2040</div>
    <div class="contact-row"><svg width="6" height="5" viewBox="0 0 10 8"><rect width="10" height="8" fill="#333"/><path d="M0 0l5 4 5-4" stroke="#fff" fill="none"/></svg>hello@willowmere.example</div>
    <div class="contact-row"><svg width="5" height="6" viewBox="0 0 8 10"><path d="M4 0a3 3 0 0 1 3 3c0 3-3 7-3 7S1 6 1 3a3 3 0 0 1 3-3z" fill="#333"/></svg>48 Alder Lane Springfield USA</div>
    <div class="social" style="margin-top:6px"><span></span><span></span><span></span><span></span></div>
  </div>

  <div class="abs copy">&copy; Willowmere 2017-2018. All rights reserved.</div>
</div>
</body>
</html>
```